Business Card Design Project

I want my business cards to stand and feel timeless! I also want people to get their hands on them and freak out over how cool these are, I already have a logo i just want a very cool card design! this is for a makeup artist and maybe one day a line of cosmetics.

Target Market(s)

I want this to target women from 18 to 45

Industry/Entity Type

Business

Font styles to use
Decorative
Script

Colors

Designer to choose colors to be used in the design.

Requirements
Must have
• it must be elegante

```html
<!DOCTYPE html>
<html lang="en">
<head>
<meta charset="utf-8">
<title>Mara Lisle Makeup – Business Card</title>
<link href="https://fonts.googleapis.com/css2?family=Julius+Sans+One&family=Cutive&family=Arimo:wght@400&display=swap" rel="stylesheet">
<style>
  :root {
    --page: #e9e7e3;
    --card: #ffffff;
    --ink: #161616;
    --ink-soft: #3a3a3a;
    --band: #0d0d0d;
    --band-text: #f4f4f4;
    --rule: #8a8a8a;
  }
  * { margin: 0; padding: 0; box-sizing: border-box; }
  html, body { width: 1200px; height: 915px; overflow: hidden; background: var(--page); }
  .canvas {
    position: relative; width: 1200px; height: 915px;
    display: flex; flex-direction: column; align-items: center; justify-content: center; gap: 45px;
  }
  .card {
    position: relative; width: 700px; height: 400px; background: var(--card);
    box-shadow: 0 6px 18px rgba(0,0,0,.12), 0 1px 3px rgba(0,0,0,.1);
    overflow: hidden;
  }
  /* front */
  .card-front .brand {
    position: absolute; left: 0; top: 0; width: 340px; height: 330px;
    display: flex; flex-direction: column; align-items: center; justify-content: center;
    font-family: "Julius Sans One", sans-serif; color: var(--ink);
  }
  .brand-name { font-size: 38px; letter-spacing: 4px; line-height: 1; }
  .brand-tag { font-size: 11px; letter-spacing: 7px; margin-top: 10px; }
  .divider {
    position: absolute; left: 340px; top: 58px; width: 1px; height: 214px; background: var(--rule);
  }
  .details { position: absolute; left: 385px; top: 78px; color: var(--ink); }
  .person-name { font-family: "Cutive", serif; font-size: 27px; line-height: 1.1; }
  .person-role { font-family: "Arimo", sans-serif; font-size: 15px; color: var(--ink-soft); margin-top: 4px; }
  .contacts { list-style: none; margin-top: 40px; font-family: "Arimo", sans-serif; font-size: 15px; color: var(--ink-soft); }
  .contacts li { display: flex; align-items: center; gap: 10px; margin-bottom: 10px; }
  .contacts svg { width: 13px; height: 13px; flex: none; }
  .address-band {
    position: absolute; left: 0; bottom: 0; width: 100%; height: 70px; background: var(--band);
    display: flex; align-items: center; justify-content: center;
    font-family: "Arimo", sans-serif; font-size: 17px; color: var(--band-text); letter-spacing: .3px;
  }
  /* back */
  .card-back { display: flex; align-items: center; justify-content: center; }
  .card-back .brand {
    display: flex; flex-direction: column; align-items: center;
    font-family: "Julius Sans One", sans-serif; color: var(--ink);
  }
  .card-back .brand-name { font-size: 62px; letter-spacing: 6px; }
  .card-back .brand-tag { font-size: 15px; letter-spacing: 11px; margin-top: 14px; }
</style>
</head>
<body>
<main class="canvas">
  <section class="card card-front" aria-label="Card front">
    <div class="brand">
      <span class="brand-name">MARA LISLE</span>
      <span class="brand-tag">MAKEUP BY</span>
    </div>
    <div class="divider"></div>
    <div class="details">
      <p class="person-name">Employee Name</p>
      <p class="person-role">Managing Director</p>
      <ul class="contacts">
        <li>
          <svg viewBox="0 0 16 16" aria-hidden="true"><path d="M4 1l2.5 3.5-1.6 1.6c.8 2 2.3 3.5 4.3 4.3l1.6-1.6L14.3 11.3 12.6 14C6.6 13.8 2.2 9.4 2 3.4z" fill="#222"/></svg>
          0012 3456 789
        </li>
        <li>
          <svg viewBox="0 0 16 16" aria-hidden="true"><rect x="1" y="3" width="14" height="10" fill="#222"/><path d="M1.5 3.5L8 9l6.5-5.5" stroke="#fff" stroke-width="1.3" fill="none"/></svg>
          info@youremail.com
        </li>
        <li>
          <svg viewBox="0 0 16 16" aria-hidden="true"><circle cx="8" cy="8" r="7" fill="#222"/><path d="M1 8h14M8 1c-3 3.5-3 10.5 0 14M8 1c3 3.5 3 10.5 0 14" stroke="#fff" stroke-width="1" fill="none"/></svg>
          www.yourwebsite.com
        </li>
      </ul>
    </div>
    <div class="address-band">Your Adress Inc 2nd Lane Ave Edison,NJ 00000</div>
  </section>

  <section class="card card-back" aria-label="Card back">
    <div class="brand">
      <span class="brand-name">MARA LISLE</span>
      <span class="brand-tag">MAKEUP BY</span>
    </div>
  </section>
</main>
</body>
</html>
```